Australian Sports Podiatry Business needs a Vantor Summerfest marketing flyer

The Stride Hub is looking for a double sided DLflyer to send out to homes which is targeted at people interested in being fit and healthy. To include:

the Vantor Summerfest logo and colours
sporty background

Are you Ready For Vantor?
Whatever Your Goals, We'll Keep You On Track
National and International Sports Experience
Lorvane Ablegames (and logo if possible)
Kestrow Unity Crown Games (and logo if poss)
Dunmere Tri-Sport Global Finals (+logo)
Dunmere Galloway Shield Tennis (+logo)

The Stride Hub name, logo, phone number 9271 6028, website www.thestridehub.example, email info@thestridehub.example

Dr Marek Ondravelli's Background:
Marek's has 20 years experience in the field of Sports Medicine and lower limb biomechanics, and he has had extensive experience with treatment of elite athletes from the Calbrook Institute of Athletics, the Fenwell Athletes Lodge, the Calbrook Stormhawks, Tolvane Harriers and the Tolvane Nightjars. He was also selected for the BRELT Medical Team to provide Podiatry Services at the Lorvane 2000 Ablegames, the 2000 GMV Global Tri-Sport Finals, the Kestrow 2006 Unity Crown Games and the Dunmere 2013 Galloway Shield. Marek now treats many athletes from all disciplines in Perth and surrounding areas.

In 1999 Marek became the Director and Senior Podiatrist for The Stride Hub in Perth, Western Australia. Since then he has also been a Director of Athletic Care Federation (ACF), WA Director for the Southern College of Lower-Limb Exercise Care (SCLEC), and an External Advisor to the Halvorne Coastal University’s Podiatric Medicine Unit. He is currently road testing minimalist running shoes for optimised performance and injury prevention.

Marek has always been involved with high level sports, having held a 4x400m Australian Record and also played 1st Division Hockey. He is now training for the Veterans Track Global Finals in October, and volunteers at Quenby Comets Junior Track. He also enjoys keeping fit by running after his 3 kids Brisa, Matilde, and Oskar.

Target Market(s)

People interested in being fit and healthy

Industry/Entity Type

Medical

Requirements
Must have
• To include:
• the Vantor Summerfest logo and colours
• sporty background
• Are you Ready For Vantor?
• Whatever Your Goals, We'll Keep You On Track
• National and International Sports Experience
• Lorvane Ablegames (and logo if possible)
• Kestrow Unity Crown Games (and logo if poss)
• Dunmere Tri-Sport Global Finals (+logo)
• Dunmere Galloway Shield Tennis (+logo)
• The Stride Hub name, logo, phone number 9271 6028, website www.thestridehub.example, email info@thestridehub.example
• Dr Marek Ondravelli's Background:
• Marek's has 20 years experience in the field of Sports Medicine and lower limb biomechanics, and he has had extensive experience with treatment of elite athletes from the Calbrook Institute of Athletics, the Fenwell Athletes Lodge, the Calbrook Stormhawks, Tolvane Harriers and the Tolvane Nightjars. He was also selected for the BRELT Medical Team to provide Podiatry Services at the Lorvane 2000 Ablegames, the 2000 GMV Global Tri-Sport Finals, the Kestrow 2006 Unity Crown Games and the Dunmere 2013 Galloway Shield. Marek now treats many athletes from all disciplines in Perth and surrounding areas.
• In 1999 Marek became the Director and Senior Podiatrist for The Stride Hub in Perth, Western Australia. Since then he has also been a Director of Athletic Care Federation (ACF), WA Director for the Southern College of Lower-Limb Exercise Care (SCLEC), and an External Advisor to the Halvorne Coastal University’s Podiatric Medicine Unit. He is currently road testing minimalist running shoes for optimised performance and injury prevention.
Nice to have
• Marek has always been involved with high level sports, having held a 4x400m Australian Record and also played 1st Division Hockey. He is now training for the Veterans Track Global Finals in October, and volunteers at Quenby Comets Junior Track. He also enjoys keeping fit by running after his 3 kids Brisa, Matilde, and Oskar.

```html
<!DOCTYPE html>
<html lang="en">
<head>
<meta charset="utf-8">
<title>The Stride Hub – Vantor Summerfest DL Flyer</title>
<link href="https://fonts.googleapis.com/css2?family=Bebas+Neue&family=Open+Sans:wght@400;600;700;800&display=swap" rel="stylesheet">
<style>
  :root {
    --stage: #e4e4e4;
    --paper: #ffffff;
    --blue: #1d5aa6;
    --blue-deep: #16468a;
    --orange: #f07a22;
    --ink: #1c1c1c;
    --body: #3a3a3a;
    --skin-light: #e9cfb4;
    --skin-dark: #a4704e;
    --green: #2e9a3e;
    --yellow: #f3b21b;
  }
  * { box-sizing: border-box; margin: 0; padding: 0; }
  html, body { width: 1200px; height: 712px; overflow: hidden; }
  body {
    background: var(--stage);
    font-family: "Open Sans", Arial, sans-serif;
    display: flex; justify-content: center; align-items: center; gap: 70px;
  }
  .flyer {
    position: relative; width: 310px; height: 660px;
    background: var(--paper); overflow: hidden;
    box-shadow: 0 6px 18px rgba(0,0,0,.18);
  }

  /* Front */
  .hero-photo {
    position: absolute; left: 0; top: 0; width: 100%; height: 340px;
    background:
      radial-gradient(ellipse 60% 40% at 65% 30%, rgba(164,112,78,.85), transparent 70%),
      radial-gradient(ellipse 50% 35% at 30% 55%, rgba(140,92,62,.8), transparent 70%),
      linear-gradient(160deg, #f3e3c8 0%, var(--skin-light) 40%, #c89a78 70%, #ecebe8 100%);
  }
  .hero-fade {
    position: absolute; left: 0; top: 250px; width: 100%; height: 100px;
    background: linear-gradient(to bottom, rgba(255,255,255,0), #fff);
  }
  .brand { position: absolute; left: 0; width: 100%; text-align: center; }
  .brand-mark {
    display: block; margin: 0 auto 4px; width: 54px; height: 54px; border-radius: 50%;
    background: var(--blue); border: 3px solid #fff;
  }
  .brand-name { font-weight: 700; font-size: 15px; color: var(--orange); }
  .front .brand { top: 300px; }
  .headline { position: absolute; top: 380px; width: 100%; text-align: center; font-family: "Bebas Neue", sans-serif; font-weight: 400; }
  .headline .line1 { font-size: 40px; color: var(--ink); line-height: 1; letter-spacing: 1px; }
  .headline .line2 { font-size: 48px; color: var(--blue); line-height: 1; letter-spacing: 1px; }
  .headline .line2 span { color: var(--orange); }
  .event-mark {
    position: absolute; top: 478px; left: 0; width: 100%;
    display: flex; justify-content: center; align-items: center; gap: 8px;
  }
  .event-dot { width: 26px; height: 26px; border-radius: 50%; }
  .event-dot.green { background: var(--green); }
  .event-dot.yellow { background: var(--yellow); }
  .event-dot.blue { background: var(--blue); }
  .tagline-band {
    position: absolute; top: 524px; left: -10px; width: 330px; height: 52px;
    background: var(--orange); transform: rotate(-6deg);
    display: flex; flex-direction: column; justify-content: center; align-items: center;
    color: #fff; font-weight: 700; font-size: 12px; line-height: 1.35; text-align: center;
  }
  .partners {
    position: absolute; top: 588px; width: 100%;
    display: flex; justify-content: space-around; align-items: center; padding: 0 26px;
  }
  .partner-badge { width: 28px; height: 28px; border-radius: 50%; background: var(--blue); opacity: .85; }
  .partner-badge:nth-child(2) { background: var(--orange); }
  .partner-badge:nth-child(3) { background: #d23b3b; }
  .partner-badge:nth-child(4) { background: var(--yellow); }
  .front-footer { position: absolute; left: 0; bottom: 0; width: 100%; height: 48px; }
  .front-footer svg { position: absolute; inset: 0; }
  .front-footer .web {
    position: absolute; bottom: 12px; width: 100%; text-align: center;
    color: #fff; font-size: 12px; letter-spacing: 3px;
  }

  /* Back */
  .back-photo {
    position: absolute; left: 0; top: 0; width: 100%; height: 160px;
    background: linear-gradient(to bottom, #d9dde2, #fff);
  }
  .back .brand { top: 18px; }
  .back .brand-mark { width: 46px; height: 46px; }
  .back .brand-name { font-size: 13px; }
  .section-title {
    position: absolute; top: 104px; left: 14px; width: 282px; height: 26px;
    background: var(--orange); color: #fff; font-weight: 800; font-size: 12px;
    display: flex; align-items: center; justify-content: center; text-transform: uppercase;
    clip-path: polygon(2% 10%, 99% 0, 97% 50%, 100% 95%, 1% 100%, 3% 55%);
  }
  .bio { position: absolute; top: 142px; left: 18px; width: 274px; }
  .bio p { font-size: 6.8px; line-height: 1.5; color: var(--body); text-align: center; margin-bottom: 7px; }
  .portrait {
    position: absolute; top: 428px; left: 115px; width: 80px; height: 80px; border-radius: 50%;
    border: 4px solid var(--blue); background: linear-gradient(#c9d3de, #8a6a55); z-index: 2;
  }
  .back-footer { position: absolute; left: 0; bottom: 0; width: 100%; height: 200px; }
  .back-footer svg { position: absolute; inset: 0; }
  .contact { position: absolute; bottom: 22px; width: 100%; text-align: center; }
  .contact .phone { color: var(--orange); font-weight: 800; font-size: 24px; }
  .contact .email { color: #fff; font-weight: 600; font-size: 13px; margin: 2px 0 10px; }
  .contact .web-pill {
    display: inline-block; background: var(--orange); color: #fff; font-size: 11px;
    letter-spacing: 2.5px; padding: 4px 18px; border-radius: 12px;
  }
</style>
</head>
<body>

<section class="flyer front">
  <div class="hero-photo" role="img" aria-label="Photo of an athlete's bare feet stretched out on a sunlit surface"></div>
  <div class="hero-fade"></div>
  <div class="brand">
    <span class="brand-mark"></span>
    <span class="brand-name">The Stride Hub</span>
  </div>
  <h1 class="headline">
    <div class="line1">Are You Ready</div>
    <div class="line2">For <span>Vantor?</span></div>
  </h1>
  <div class="event-mark" role="img" aria-label="Vantor Summerfest event badge">
    <span class="event-dot green"></span><span class="event-dot yellow"></span><span class="event-dot blue"></span>
  </div>
  <div class="tagline-band">
    <span>Whatever Your Goals, We'll Keep You On Track</span>
    <span>National and International Sports Experience</span>
  </div>
  <div class="partners" role="img" aria-label="Partner event badges">
    <span class="partner-badge"></span><span class="partner-badge"></span>
    <span class="partner-badge"></span><span class="partner-badge"></span>
  </div>
  <footer class="front-footer">
    <svg width="310" height="48" viewBox="0 0 310 48" preserveAspectRatio="none">
      <polygon fill="var(--blue)" points="0,14 18,8 34,16 52,6 70,12 92,4 110,14 132,8 150,16 172,5 194,12 214,6 236,15 256,7 278,13 296,4 310,10 310,48 0,48"/>
    </svg>
    <div class="web">www.thestridehub.example</div>
  </footer>
</section>

<section class="flyer back">
  <div class="back-photo" role="img" aria-label="Faded photo of a runner on a track"></div>
  <div class="brand">
    <span class="brand-mark"></span>
    <span class="brand-name">The Stride Hub</span>
  </div>
  <h2 class="section-title">Dr Marek Ondravelli's Background:</h2>
  <div class="bio">
    <p>Marek has 20 years experience in the field of Sports Medicine and lower limb biomechanics, and he has had extensive experience with treatment of elite athletes from the Calbrook Institute of Athletics, the Fenwell Athletes Lodge, the Calbrook Stormhawks, Tolvane Harriers and the Tolvane Nightjars. He was also selected for the BRELT Medical Team to provide Podiatry Services at the Lorvane 2000 Ablegames, the 2000 GMV Global Tri-Sport Finals, the Kestrow 2006 Unity Crown Games and the Dunmere 2013 Galloway Shield. Marek now treats many athletes from all disciplines in Perth and surrounding areas.</p>
    <p>In 1999 Marek became the Director and Senior Podiatrist for The Stride Hub in Perth, Western Australia. Since then he has also been a Director of Athletic Care Federation (ACF), WA Director for the Southern College of Lower-Limb Exercise Care (SCLEC), and an External Advisor to the Halvorne Coastal University's Podiatric Medicine Unit. He is currently road testing minimalist running shoes for optimised performance and injury prevention.</p>
    <p>Marek has always been involved with high level sports, having held a 4x400m Australian Record and also played 1st Division Hockey. He is now training for the Veterans Track Global Finals in October, and volunteers at Quenby Comets Junior Track. He also enjoys keeping fit by running after his 3 kids Brisa, Matilde, and Oskar.</p>
  </div>
  <div class="portrait" role="img" aria-label="Portrait photo of Dr Marek Ondravelli"></div>
  <footer class="back-footer">
    <svg width="310" height="200" viewBox="0 0 310 200" preserveAspectRatio="none">
      <polygon fill="var(--blue-deep)" points="0,36 20,24 40,34 62,20 84,30 104,16 126,28 150,14 172,26 196,18 218,30 240,16 262,26 284,18 310,28 310,200 0,200"/>
      <polygon fill="var(--blue)" points="0,50 24,40 46,48 70,36 96,46 120,38 146,48 170,34 196,44 222,36 248,46 272,38 296,46 310,40 310,200 0,200"/>
    </svg>
    <div class="contact">
      <div class="phone">Call Us: 9271 6028</div>
      <div class="email">info@thestridehub.example</div>
      <div class="web-pill">www.thestridehub.example</div>
    </div>
  </footer>
</section>

</body>
</html>
```